Tailbrook Website Design

Need a website for a Dog Grooiming business. Please make it simular to these:

https://www.furvanto.com
https://haulnorix.com
https://meadowpetrin.com
https://www.drivelumo.com/search/

```html
<!DOCTYPE html>
<html lang="en">
<head>
<meta charset="utf-8">
<title>Tailbrook – Dog Grooming</title>
<link href="https://fonts.googleapis.com/css2?family=Poppins:wght@400;500;600&family=Ubuntu:wght@400;500;700&display=swap" rel="stylesheet">
<style>
:root{
  --navy:#0b3d7c;
  --sky:#0d9fd2;
  --sky-deep:#0a8fc2;
  --mist:#e7f5fb;
  --mist-2:#d6eef8;
  --ink:#222a33;
  --text:#3d4650;
  --white:#ffffff;
  --line:#dfe7ee;
}
*{box-sizing:border-box;margin:0;padding:0}
html,body{width:1200px;height:4202px;overflow:hidden}
body{position:relative;background:var(--white);font-family:"Poppins",sans-serif;color:var(--text)}
.abs{position:absolute}
.h-title{font-family:"Ubuntu",sans-serif;font-size:37px;color:var(--ink);font-weight:700;position:absolute;white-space:nowrap}
.h-title span{color:var(--navy);font-weight:400}
.center{left:0;width:1200px;text-align:center}
.divider{position:absolute;height:14px;width:100px}
.divider i{position:absolute;top:6px;height:2px;width:38px;background:var(--navy)}
.divider i:first-child{left:0}.divider i:last-child{right:0}
.divider b{position:absolute;left:42px;top:0;width:16px;height:14px;border-radius:50%;background:var(--sky)}
.btn{position:absolute;background:var(--navy);color:var(--white);border-radius:20px;font-size:13px;font-weight:500;display:flex;align-items:center;justify-content:center;white-space:nowrap}
.photo{position:absolute}

/* top bar */
.topbar{position:absolute;left:0;top:0;width:1200px;height:36px;background:var(--sky);color:var(--white);font-size:13px}
.topbar .item{position:absolute;top:0;height:36px;display:flex;align-items:center;gap:10px;white-space:nowrap}
.ring{width:26px;height:26px;border:1.5px solid var(--white);border-radius:50%;display:flex;align-items:center;justify-content:center}
.social{position:absolute;display:flex;gap:9px}
.social i{width:26px;height:26px;border:1.5px solid var(--white);border-radius:50%}

/* nav */
.nav{position:absolute;left:0;top:36px;width:1200px;height:62px;background:var(--white);box-shadow:0 2px 8px rgba(0,0,0,.06)}
.brand-mark{position:absolute;border-radius:50%;background:var(--navy)}
.brand-name{position:absolute;font-family:"Poppins",sans-serif;font-weight:600;color:var(--sky);white-space:nowrap}
.nav a{position:absolute;top:22px;font-size:13px;color:var(--ink);text-decoration:none;white-space:nowrap}
.nav a.active{color:var(--navy);font-weight:600}
.nav a.active::after{content:"";position:absolute;left:0;right:0;bottom:-18px;height:3px;background:var(--sky)}

/* hero */
.hero-kicker{left:161px;top:240px;font-size:24px;color:var(--ink);font-family:"Ubuntu",sans-serif}
.hero-title{left:158px;top:268px;font-size:54px;color:var(--sky);font-family:"Ubuntu",sans-serif;font-weight:500;letter-spacing:1px;white-space:nowrap}
.hero-copy{left:161px;top:333px;width:300px;font-size:11.5px;line-height:22px;text-align:justify;color:var(--ink)}
.slide-arrow{position:absolute;top:278px;width:42px;height:80px;background:var(--sky);color:var(--white);display:flex;align-items:center;justify-content:center;font-size:20px}

/* about */
.about-copy{left:651px;top:760px;width:384px;font-size:12.5px;line-height:27px;text-align:justify}
.tick-list{position:absolute;left:653px;list-style:none;font-size:12.5px;font-weight:600;color:var(--ink)}
.tick-list li{height:39px;display:flex;align-items:center;gap:8px;white-space:nowrap}
.tick-list li::before{content:"";width:14px;height:12px;border-radius:50%;background:var(--sky)}

/* services */
.card{position:absolute;width:429px;height:134px;background:var(--white);box-shadow:0 3px 12px rgba(11,61,124,.08)}
.card .icon{position:absolute;left:14px;top:34px;width:60px;height:60px;border-radius:8px;background:var(--mist)}
.card h3{position:absolute;left:89px;top:18px;font-family:"Ubuntu",sans-serif;font-size:17px;font-weight:500;color:var(--ink);white-space:nowrap}
.card.feature h3{color:var(--navy)}
.card p{position:absolute;left:89px;top:46px;width:318px;font-size:12px;line-height:24px;color:var(--text)}
.card .more{position:absolute;left:90px;top:100px;font-size:12px;color:var(--ink);display:flex;align-items:center;gap:10px;white-space:nowrap}
.card.feature .more{color:var(--navy);font-weight:600}

/* testimonials */
.quote-copy{left:280px;top:2174px;width:640px;font-size:12.5px;line-height:24px;text-align:center;color:var(--ink)}
.quote-mark{position:absolute;font-family:"Ubuntu",sans-serif;font-size:130px;color:var(--mist-2);line-height:1}
.avatar{position:absolute;border-radius:50%;border:3px solid var(--white);box-shadow:0 2px 10px rgba(0,0,0,.12)}

/* contact */
.panel-form{position:absolute;left:199px;top:2836px;width:396px;height:391px;background:var(--sky-deep)}
.panel-hours{position:absolute;left:595px;top:2836px;width:404px;height:391px;background:var(--navy)}
.panel-title{position:absolute;left:0;width:100%;top:34px;text-align:center;color:var(--white);font-family:"Ubuntu",sans-serif;font-size:18px;font-weight:500}
.field{position:absolute;left:91px;width:212px;height:36px;background:var(--white);border-radius:3px;font-size:12px;color:var(--ink);display:flex;align-items:center;padding-left:38px;white-space:nowrap}
.field::before{content:"";position:absolute;left:14px;top:12px;width:12px;height:12px;border-radius:2px;background:#9aa7b3}
.hours{position:absolute;left:62px;top:80px;width:282px;list-style:none;color:var(--white);font-size:12px}
.hours li{height:36px;display:flex;align-items:center;border-bottom:1px solid rgba(255,255,255,.35);white-space:nowrap}
.hours li:last-child{border-bottom:none}
.hours span{flex:none;width:166px}
.hours em{font-style:normal;flex:none}
.hours b{font-weight:600}

/* map card */
.map-card{position:absolute;left:448px;top:3505px;width:225px;height:111px;background:var(--white);box-shadow:0 4px 14px rgba(0,0,0,.15);padding:10px 14px}
.pin-row{display:flex;gap:8px;align-items:flex-start;font-size:10.5px;color:var(--navy);line-height:14px;margin-top:5px}
.pin-row i{flex:none;width:22px;height:22px;border-radius:50%;background:var(--navy)}

/* footer */
.foot-copy{left:161px;top:4006px;width:265px;font-size:12px;line-height:30px;color:var(--ink)}
.foot-head{position:absolute;font-family:"Ubuntu",sans-serif;font-size:22px;color:var(--ink);font-weight:500;white-space:nowrap}
.foot-head span{color:var(--navy)}
.foot-rule{position:absolute;height:14px;width:88px}
.foot-rule b{position:absolute;left:0;top:0;width:16px;height:14px;border-radius:50%;background:var(--sky)}
.foot-rule i{position:absolute;left:28px;top:6px;width:60px;height:2px;background:var(--navy)}
.links{position:absolute;left:543px;top:3950px;list-style:none;font-size:13px;color:var(--ink)}
.links li{height:31px;display:flex;align-items:center}
.links li::before{content:"»";margin-right:9px;color:var(--text)}
.contact-row{position:absolute;left:799px;display:flex;gap:12px;font-size:13.5px;color:var(--ink);line-height:17px;align-items:center;white-space:nowrap}
.contact-row i{flex:none;width:30px;height:30px;border:1.5px solid var(--navy);border-radius:50%;display:flex;align-items:center;justify-content:center}
.bottombar{position:absolute;left:0;top:4157px;width:1200px;height:45px;background:var(--sky);color:var(--white);font-size:12.5px}
</style>
</head>
<body>

<header class="topbar">
  <div class="item" style="left:352px">
    <span class="ring"><svg width="10" height="13" viewBox="0 0 10 13"><path d="M5 0a5 5 0 0 0-5 5c0 3.5 5 8 5 8s5-4.5 5-8a5 5 0 0 0-5-5zm0 7a2 2 0 1 1 0-4 2 2 0 0 1 0 4z" fill="#fff"/></svg></span>
    123, Building Name, Street, City - 123 456
  </div>
  <div class="item" style="left:730px;font-weight:600;font-size:14px">
    <span class="ring"><svg width="12" height="12" viewBox="0 0 12 12"><path d="M2.5 0.5l2 2.5-1.2 1.5c.8 1.7 2 2.9 3.7 3.7L8.5 7l2.5 2-1.5 2.5C4.8 11 1 7.2.5 2z" fill="#fff"/></svg></span>
    123 - 456 - 789
  </div>
  <div class="social" style="left:940px;top:5px"><i></i><i></i><i></i></div>
</header>

<nav class="nav">
  <div class="brand-mark" style="left:181px;top:-28px;width:50px;height:50px;border:3px solid #fff"></div>
  <div class="brand-name" style="left:164px;top:32px;font-size:16px">Tailbrook</div>
  <a class="active" style="left:375px">Home</a>
  <a style="left:466px">About Us</a>
  <a style="left:576px">Services</a>
  <a style="left:680px">Testimonials</a>
  <a style="left:813px">Contact Us</a>
  <span class="btn" style="left:918px;top:13px;width:120px;height:36px">Book Online</span>
</nav>

<section>
  <svg class="abs" style="left:0;top:98px" width="1200" height="520" viewBox="0 0 1200 520">
    <path d="M0 0H1200V470C1080 505 960 520 820 492 680 465 560 420 430 430 280 442 150 505 0 480Z" fill="var(--mist)"/>
  </svg>
  <div class="photo" role="img" aria-label="Spaniel sitting in front of a pale blue circle" style="left:603px;top:139px;width:440px;height:440px;border-radius:50%;background:radial-gradient(circle at 55% 45%,#b86a3c 0 22%,#f3ede6 38%,#d4ecf7 62%,#e2f3fa 100%)"></div>
  <div class="slide-arrow" style="left:0;border-radius:0 40px 40px 0">←</div>
  <div class="slide-arrow" style="right:0;border-radius:40px 0 0 40px">→</div>
  <div class="abs hero-kicker">WELCOME TO</div>
  <div class="abs hero-title">TAILBROOK</div>
  <p class="abs hero-copy">Lorem ipsum dolor sit amet, consectetuer adipiscing elit, sed diam nonummy nibh euismod tincidunt ut laoreet dolore magna aliquam erat.</p>
  <span class="btn" style="left:161px;top:414px;width:121px;height:36px">Book Online</span>
</section>

<section>
  <div class="photo" role="img" aria-label="Small terrier being groomed with comb and scissors" style="left:155px;top:668px;width:440px;height:424px;border-radius:46% 54% 42% 58% / 50% 40% 60% 50%;border:4px solid #4ab0e2;background:linear-gradient(135deg,#c9c4bd,#8a6a4a 45%,#d8d2cb)"></div>
  <div class="h-title" style="left:651px;top:668px">About <span>Us</span></div>
  <div class="abs" style="left:651px;top:722px;width:88px;height:14px">
    <b style="position:absolute;left:0;top:0;width:16px;height:14px;border-radius:50%;background:var(--sky)"></b>
    <i style="position:absolute;left:28px;top:6px;width:60px;height:2px;background:var(--navy)"></i>
  </div>
  <p class="abs about-copy">Lorem ipsum dolor sit amet, consectetuer adipiscing elit, sed diam nonummy nibh euismod tincidunt ut laoreet dolore magna aliquam erat volutpat. Ut wisi enim ad minim veniam, quis nostrud exerci tation ullamcorper suscipit lobortis nisl ut aliquip ex ea commodo consequat. Duis autem vel.</p>
  <ul class="tick-list" style="top:898px">
    <li>Lorem ipsum dolor sit amet, consectetu.</li>
    <li>Lorem ipsum dolor sit amet, consectetu.</li>
    <li>Lorem ipsum dolor sit amet, consectetu.</li>
  </ul>
  <span class="btn" style="left:654px;top:1038px;width:120px;height:36px">Read More</span>
</section>

<section>
  <svg class="abs" style="left:0;top:1130px" width="1200" height="840" viewBox="0 0 1200 840">
    <path d="M0 5C140 40 260 60 420 40 600 15 760 -5 920 20 1040 40 1120 60 1200 50V760C1060 800 900 790 740 770 560 748 420 720 260 740 150 755 70 790 0 805Z" fill="var(--mist)"/>
  </svg>
  <div class="h-title center" style="top:1266px">Our <span>Services</span></div>
  <div class="divider" style="left:550px;top:1320px"><i></i><b></b><i></i></div>

  <div class="card feature" style="left:161px;top:1368px">
    <div class="icon" role="img" aria-label="Line icon of a dog with a groomed haircut"></div>
    <h3>Hair Cut</h3>
    <p>Lorem ipsum dolor sit amet, consectetuer adipiscing elit, sed diam nonummy nibh euismod tincidunt...</p>
    <span class="more">Read More <svg width="20" height="8"><path d="M0 4H18M14 0l5 4-5 4" stroke="currentColor" stroke-width="2" fill="none"/></svg></span>
  </div>
  <div class="card" style="left:610px;top:1368px">
    <div class="icon" role="img" aria-label="Line icon of a dog showing clean teeth"></div>
    <h3>Teeth Cleaning</h3>
    <p>Lorem ipsum dolor sit amet, consectetuer adipiscing elit, sed diam nonummy nibh euismod tincidunt...</p>
    <span class="more">Read More <svg width="20" height="8"><path d="M0 4H18M14 0l5 4-5 4" stroke="currentColor" stroke-width="2" fill="none"/></svg></span>
  </div>
  <div class="card" style="left:161px;top:1522px">
    <div class="icon" role="img" aria-label="Line icon of a dog having its ears cleaned"></div>
    <h3>Ear Cleaning</h3>
    <p>Lorem ipsum dolor sit amet, consectetuer adipiscing elit, sed diam nonummy nibh euismod tincidunt...</p>
    <span class="more">Read More <svg width="20" height="8"><path d="M0 4H18M14 0l5 4-5 4" stroke="currentColor" stroke-width="2" fill="none"/></svg></span>
  </div>
  <div class="card" style="left:610px;top:1522px">
    <div class="icon" role="img" aria-label="Line icon of nail clippers on a paw"></div>
    <h3>Nail Clipping</h3>
    <p>Lorem ipsum dolor sit amet, consectetuer adipiscing elit, sed diam nonummy nibh euismod tincidunt...</p>
    <span class="more">Read More <svg width="20" height="8"><path d="M0 4H18M14 0l5 4-5 4" stroke="currentColor" stroke-width="2" fill="none"/></svg></span>
  </div>
  <div class="card" style="left:161px;top:1676px">
    <div class="icon" role="img" aria-label="Line icon of a bath tub with shampoo bottles"></div>
    <h3>Bath With Shampoo &amp; Conditioner</h3>
    <p>Lorem ipsum dolor sit amet, consectetuer adipiscing elit, sed diam nonummy nibh euismod tincidunt...</p>
    <span class="more">Read More <svg width="20" height="8"><path d="M0 4H18M14 0l5 4-5 4" stroke="currentColor" stroke-width="2" fill="none"/></svg></span>
  </div>
  <div class="card" style="left:610px;top:1676px">
    <div class="icon" role="img" aria-label="Line icon of a spray bottle"></div>
    <h3>Mouth Spray</h3>
    <p>Lorem ipsum dolor sit amet, consectetuer adipiscing elit, sed diam nonummy nibh euismod tincidunt...</p>
    <span class="more">Read More <svg width="20" height="8"><path d="M0 4H18M14 0l5 4-5 4" stroke="currentColor" stroke-width="2" fill="none"/></svg></span>
  </div>
  <span class="btn" style="left:540px;top:1842px;width:120px;height:36px">View All</span>
</section>

<section>
  <div class="h-title center" style="top:2081px">Client <span>Testimonials</span></div>
  <div class="divider" style="left:550px;top:2135px"><i></i><b></b><i></i></div>
  <div class="quote-mark" style="left:208px;top:2140px">“</div>
  <div class="quote-mark" style="left:876px;top:2200px">”</div>
  <p class="abs quote-copy">Lorem Ipsum is simply dummy text of the printing and typesetting industry. Lorem Ipsum has been the industry's standard dummy text ever since the 1500s, when an unknown printer took a galley of type and scrambled it to make a type specimen book. It has survived not only five centuries, but also the leap into electronic typesetting, remaining essentially unchanged.</p>
  <svg class="abs" style="left:400px;top:2328px" width="16" height="10"><path d="M16 5H2M6 1L1 5l5 4" stroke="#8a949e" stroke-width="1.5" fill="none"/></svg>
  <svg class="abs" style="left:792px;top:2328px" width="16" height="10"><path d="M0 5H14M10 1l5 4-5 4" stroke="var(--sky)" stroke-width="1.5" fill="none"/></svg>
  <div class="avatar" role="img" aria-label="Client portrait" style="left:453px;top:2295px;width:76px;height:76px;background:linear-gradient(160deg,#f1e2d3,#b98a6a)"></div>
  <div class="avatar" role="img" aria-label="Client portrait" style="left:554px;top:2286px;width:94px;height:94px;background:linear-gradient(160deg,#e4ecf1,#6a5a52)"></div>
  <div class="avatar" role="img" aria-label="Client portrait" style="left:676px;top:2295px;width:76px;height:76px;background:linear-gradient(160deg,#f7eadf,#d9b88c)"></div>
  <div class="abs center" style="top:2385px;font-size:15px;font-weight:500;color:var(--ink)">Lorem Ipsum</div>
</section>

<section>
  <svg class="abs" style="left:0;top:2460px" width="1200" height="900" viewBox="0 0 1200 900">
    <path d="M0 20C160 0 320 30 520 45 720 60 900 20 1200 40V900H0Z" fill="var(--mist)"/>
  </svg>
  <div class="h-title center" style="top:2600px">Get In <span>Touch</span></div>
  <div class="divider" style="left:550px;top:2653px"><i></i><b></b><i></i></div>
  <div class="photo" role="img" aria-label="Row of five dogs peeking over the booking panel" style="left:318px;top:2690px;width:554px;height:146px;border-radius:60px 60px 0 0;background:linear-gradient(90deg,#5b3a2a,#e8dccd 25%,#efe6dc 45%,#b08a5d 65%,#8f6232 85%,#e9ddd0)"></div>
  <div class="photo" role="img" aria-label="Pomeranian dog" style="left:0;top:3138px;width:179px;height:220px;border-radius:50% 50% 0 0;background:linear-gradient(170deg,#e2a25a,#b8692a)"></div>
  <div class="photo" role="img" aria-label="Beagle dog standing" style="left:1027px;top:3016px;width:173px;height:326px;border-radius:50% 40% 10% 30%;background:linear-gradient(170deg,#f1ece6,#a7652f 50%,#efe9e2)"></div>

  <div class="panel-form">
    <svg class="abs" style="left:0;top:0" width="36" height="36"><path d="M0 36L36 0H0Z" fill="#0c78a6"/></svg>
    <div class="panel-title">Book An Appointment</div>
    <div class="field" style="top:77px">Name*</div>
    <div class="field" style="top:122px">Phone*</div>
    <div class="field" style="top:167px">Email*</div>
    <div class="field" style="top:211px">Appointment Date</div>
    <div class="field" style="top:256px">Appointment Time</div>
    <span class="btn" style="left:91px;top:317px;width:121px;height:36px;background:var(--navy)">Submit Now</span>
  </div>
  <div class="panel-hours">
    <svg class="abs" style="right:0;bottom:0" width="36" height="36"><path d="M36 0L0 36H36Z" fill="#082d5c"/></svg>
    <div class="panel-title">Working Hours</div>
    <ul class="hours">
      <li><span>Monday</span><em>09.00am - 06.00pm</em></li>
      <li><span>Tuesday</span><em>09.00am - 06.00pm</em></li>
      <li><span>Wednesday</span><em>09.00am - 06.00pm</em></li>
      <li><span>Thursday</span><em>09.00am - 06.00pm</em></li>
      <li><span>Friday</span><em>09.00am - 06.00pm</em></li>
      <li><span>Saturday</span><em>09.00am - 11.30am</em></li>
      <li><span>Sunday</span><b>Closed</b></li>
    </ul>
  </div>
</section>

<section>
  <svg class="abs" style="left:0;top:3310px" width="1200" height="500" viewBox="0 0 1200 500" role="img" aria-label="Street map showing the salon location">
    <path d="M0 40C150 20 300 70 520 60 760 50 950 5 1200 30V470C1000 500 780 470 560 490 340 505 160 470 0 485Z" fill="#e9ebed"/>
  </svg>
  <div class="map-card">
    <div style="font-family:'Poppins',sans-serif;font-weight:600;font-size:15px;color:var(--sky)">Tailbrook</div>
    <div class="pin-row"><i></i>123, Building Name, Street, City - 123 456</div>
    <div class="pin-row" style="align-items:center;font-weight:600"><i></i>123 - 456 - 789</div>
  </div>
  <svg class="abs" style="left:683px;top:3573px" width="24" height="32"><path d="M12 0A12 12 0 0 0 0 12c0 9 12 20 12 20s12-11 12-20A12 12 0 0 0 12 0zm0 17a5 5 0 1 1 0-10 5 5 0 0 1 0 10z" fill="var(--navy)"/></svg>
</section>

<footer>
  <div class="brand-mark" style="left:163px;top:3884px;width:72px;height:72px"></div>
  <div class="brand-name" style="left:161px;top:3962px;font-size:24px">Tailbrook</div>
  <p class="abs foot-copy">Lorem Ipsum is simply dummy text of the printing and typesetting industry. Lorem Ipsum has been the industry's standard dummy text ever since the 1500s.</p>

  <div class="foot-head" style="left:543px;top:3876px">Quick <span>Links</span></div>
  <div class="foot-rule" style="left:545px;top:3914px"><b></b><i></i></div>
  <ul class="links">
    <li>Home</li><li>About Us</li><li>Services</li><li>Blog</li><li>Our Team</li><li>Contact Us</li>
  </ul>

  <div class="foot-head" style="left:799px;top:3876px">Contact <span>Details</span></div>
  <div class="foot-rule" style="left:801px;top:3914px"><b></b><i></i></div>
  <div class="contact-row" style="top:3955px"><i><svg width="10" height="13" viewBox="0 0 10 13"><path d="M5 0a5 5 0 0 0-5 5c0 3.5 5 8 5 8s5-4.5 5-8a5 5 0 0 0-5-5zm0 7a2 2 0 1 1 0-4 2 2 0 0 1 0 4z" fill="var(--navy)"/></svg></i>123, Building Name, Street,<br>City - 123 456</div>
  <div class="contact-row" style="top:4010px"><i><svg width="12" height="12" viewBox="0 0 12 12"><path d="M2.5 0.5l2 2.5-1.2 1.5c.8 1.7 2 2.9 3.7 3.7L8.5 7l2.5 2-1.5 2.5C4.8 11 1 7.2.5 2z" fill="var(--navy)"/></svg></i>123 456 7890</div>
  <div class="contact-row" style="top:4063px"><i><svg width="13" height="10" viewBox="0 0 13 10"><rect width="13" height="10" rx="1" fill="var(--navy)"/><path d="M0 1l6.5 5L13 1" stroke="#fff" fill="none"/></svg></i>info@tailbrook.com</div>

  <div class="photo" role="img" aria-label="Pomeranian dog lying down" style="left:994px;top:3977px;width:206px;height:180px;border-radius:55% 45% 0 0;background:linear-gradient(170deg,#e3a55d,#b46b2c)"></div>

  <div class="bottombar">
    <div class="abs" style="left:161px;top:14px">Copyright 2021. Tailbrook. All Rights Reserved.</div>
    <div class="social" style="left:940px;top:9px"><i></i><i></i><i></i></div>
  </div>
</footer>

</body>
</html>
```